Mobile phone signal boosting solutions needs a website

We need a website design for the reselling of a mobile signal boosting product set. These solutions are Travik exempt and will provide an indoor signal for mobile phones. We would like to see designs that incorporate the colours and feel of our logo. The domain will be
nestorbolt.com / co.uk
Overview of the company and how it is to be used: Nestor Bolt (domain name) will work with business and end user to provide mobile signal boosting – where people struggle indoors with a mobile signal our solutions will help by finding the smallest signal and boosting it, allowing users to use voice and data over their mobile network (please note this is not wireless signal boosting)
Number of Pages:
-Home
-Solutions / How it works
-Case Studies
-Contact
Text content: Currently just use placeholders
Technical specs : Wordpress and ability to use CMS if that’s relevant
Target Market(s)
Business professional all markets /high end residential
Coding
Coded - Design and coding required
Number of Pages Required
4 page
Look and feel

```html
<!DOCTYPE html>
<html lang="en">
<head>
<meta charset="UTF-8">
<title>Nestor Bolt – Mobile Signal Booster</title>
<link href="https://fonts.googleapis.com/css2?family=Poppins:wght@300;400;500;600;700&display=swap" rel="stylesheet">
<style>
:root{
  --orange:#f8ad36;
  --orange-band:#efab3f;
  --orange-deep:#e9962a;
  --ink:#1d1d1d;
  --text:#3c3c3c;
  --muted:#5a5a5a;
  --hero-bg:#e8e9eb;
  --cream:#fdf5ea;
  --white:#ffffff;
  --footer:#1c1c1c;
  --link:#3f8fc9;
  --line:#cfcfcf;
}
*{box-sizing:border-box;margin:0;padding:0}
html,body{width:1200px;height:4335px;overflow:hidden}
body{font-family:'Poppins',sans-serif;color:var(--text);background:var(--white);position:relative}
section,header,footer{position:absolute;left:0;width:1200px}
.abs{position:absolute}
.btn{position:absolute;background:var(--orange);color:var(--white);font-weight:600;font-size:15px;letter-spacing:.5px;display:flex;align-items:center;justify-content:center;border-radius:3px;text-transform:uppercase}
.section-title{position:absolute;left:0;width:1200px;text-align:center;font-weight:500;color:var(--ink);font-size:40px}
.section-sub{position:absolute;left:0;width:1200px;text-align:center;font-size:14px;color:var(--text);line-height:29px}

/* header + hero */
.hero{top:0;height:665px;background:var(--hero-bg);overflow:hidden}
.brand{position:absolute;left:99px;top:62px;display:flex;align-items:center;gap:10px;font-weight:600;font-size:24px;color:var(--ink)}
.brand-dot{width:16px;height:16px;background:var(--orange)}
.nav{position:absolute;top:32px;left:561px;font-size:15px;font-weight:500;color:var(--ink)}
.nav a{color:inherit;text-decoration:none;position:absolute;white-space:nowrap}
.nav-contact{left:953px;top:21px;width:147px;height:43px;font-size:15px}
.hero-photo{left:555px;top:67px;width:645px;height:598px;background:linear-gradient(160deg,#d9dadc 0%,#c9c4bd 40%,#b8b0a6 60%,#d7d8da 100%);clip-path:polygon(0 0,100% 0,100% 78%,75% 100%,0 100%)}
.social{left:38px;top:210px;display:flex;flex-direction:column;gap:16px}
.social span{display:block;width:12px;height:12px;border-radius:50%;background:var(--ink)}
.follow-line{left:44px;top:320px;width:1px;height:70px;background:var(--ink)}
.follow{left:16px;top:440px;transform:rotate(-90deg);font-size:12px;letter-spacing:4px;color:var(--ink);white-space:nowrap}
.hero-title{left:97px;top:256px;font-size:57px;font-weight:700;color:var(--ink);letter-spacing:.5px}
.hero-sub{left:99px;top:326px;font-size:29px;font-weight:400;color:var(--ink)}
.hero-text{left:99px;top:376px;width:430px;font-size:16px;line-height:27px;color:var(--ink)}

/* how it works */
.how{top:665px;height:589px;background:var(--white)}
.step{position:absolute;top:227px;width:230px}
.step-icon{width:94px;height:94px;border-radius:50%;background:#fdf0df}
.step h3{margin-top:24px;font-size:23px;font-weight:600;color:var(--ink)}
.step p{margin-top:12px;font-size:13.5px;line-height:27px;color:var(--muted)}
.step-arrow{position:absolute;top:258px}

/* about */
.about{top:1254px;height:533px;background:var(--cream)}
.about-photo{left:99px;top:76px;width:478px;height:382px;background:linear-gradient(150deg,#1b2a52 0%,#3b5a8c 45%,#7d8aa5 60%,#1b2440 100%)}
.about h2{position:absolute;left:653px;top:82px;font-size:40px;font-weight:500;color:var(--ink)}
.about p{position:absolute;left:656px;top:138px;width:448px;font-size:14px;line-height:29.3px;color:var(--muted)}

/* boost band */
.boost{top:1787px;height:406px;background:linear-gradient(180deg,var(--orange-band),#eea63a)}
.boost h2{position:absolute;left:0;width:1200px;top:70px;text-align:center;color:var(--white);font-weight:400;font-size:37px}
.building{position:absolute;top:174px;width:260px;text-align:center;color:var(--white)}
.building .circle{width:84px;height:84px;border-radius:50%;background:var(--orange-deep);margin:0 auto;display:flex;align-items:center;justify-content:center}
.building h3{margin-top:28px;font-size:22px;font-weight:600}
.building p{margin-top:2px;font-size:16px;font-weight:300}

/* help */
.help{top:2193px;height:463px;background:var(--hero-bg)}
.help-photo{left:0;top:-22px;width:540px;height:485px;background:linear-gradient(120deg,#d6d7d9 0%,#c8b8a6 40%,#eeeeee 60%,#d2d3d5 100%)}
.help h2{position:absolute;left:677px;top:90px;width:440px;font-size:33px;line-height:36px;font-weight:600;color:var(--ink)}
.help p{position:absolute;left:677px;top:212px;width:424px;font-size:13.5px;line-height:31px;color:var(--text);text-align:justify}

/* case studies */
.cases{top:2656px;height:718px;background:var(--cream)}
.case{position:absolute;background:var(--white)}
.case h3{font-size:18px;line-height:26px;font-weight:600;color:var(--ink)}
.case p{margin-top:16px;font-size:12.5px;line-height:26px;color:var(--muted);text-align:justify}
.case-text{position:absolute;padding:0 20px}
.case-img{position:absolute}

/* contact */
.contact{top:3374px;height:623px;background:var(--white)}
.field{position:absolute;border:1px solid #c9c9c9;font-size:14px;color:var(--muted);padding:14px 12px;background:var(--white)}
.info-card{position:absolute;left:719px;top:191px;width:382px;height:267px;background:var(--white);box-shadow:0 6px 22px rgba(0,0,0,.14);border-radius:4px;padding:30px 22px;font-size:16px;color:var(--ink);line-height:31px}
.info-card .link{color:var(--link)}

/* footer */
.footer{top:3997px;height:338px;background:var(--footer);color:var(--white)}
.footer-brand{position:absolute;left:101px;top:150px;font-size:34px;font-weight:500;color:var(--white)}
.fcol{position:absolute;top:65px}
.fcol h4{font-size:18px;font-weight:600;letter-spacing:.3px}
.fcol ul{list-style:none;margin-top:12px}
.fcol li{font-size:13px;line-height:33px;display:flex;align-items:center;gap:8px}
.footer-rule{position:absolute;left:99px;top:273px;width:1002px;height:1px;background:#3a3a3a}
.copy{position:absolute;left:0;width:1200px;top:294px;text-align:center;font-size:13px}
</style>
</head>
<body>

<section class="hero">
  <div class="brand"><span class="brand-dot"></span>Nestor Bolt</div>
  <nav class="nav">
    <a href="#" style="left:0">HOME</a>
    <a href="#" style="left:86px">HOW IT WORKS</a>
    <a href="#" style="left:246px">CASE STUDIES</a>
  </nav>
  <a class="btn nav-contact">Contact</a>

  <div class="abs hero-photo" role="img" aria-label="Smiling woman giving a thumbs up and holding a phone, with yellow and black signal bars behind her"></div>

  <div class="abs social"><span></span><span></span><span></span><span></span></div>
  <div class="abs follow-line"></div>
  <div class="abs follow">FOLLOW US</div>

  <h1 class="abs hero-title">NESTOR BOLT</h1>
  <div class="abs hero-sub">MOBILE SIGNAL BOOSTER</div>
  <p class="abs hero-text">Lorem ipsum dolor sit amet, cetur adipiscing elit, sed do eiusmod tempor</p>
  <a class="btn" style="left:99px;top:449px;width:148px;height:44px">Get Started</a>
</section>

<section class="how">
  <h2 class="section-title" style="top:68px">How It Works</h2>
  <p class="section-sub" style="top:118px">Lorem ipsum dolor sit amet, consectetur adipiscing elit, sed do eiusmod tempor incididunt ut labore et<br>dolore magna aliqua. Quis ipsum suspendisse ultrices gravida.</p>

  <div class="step" style="left:99px"><div class="step-icon" role="img" aria-label="Signal tower icon"></div><h3>Receive Signal</h3><p>At vero eos et accusaus et iusto odio dis ducimus qui blangditiis praentium voluptatum deleniti atque corrupti quos</p></div>
  <div class="step" style="left:360px"><div class="step-icon" role="img" aria-label="Rocket icon"></div><h3>Boost Signal</h3><p>At vero eos et accusaus et iusto odio dis ducimus qui blangditiis praentium voluptatum deleniti atque corrupti quos</p></div>
  <div class="step" style="left:621px"><div class="step-icon" role="img" aria-label="Signal booster unit icon"></div><h3>Expands Signal</h3><p>At vero eos et accusaus et iusto odio dis ducimus qui blangditiis praentium voluptatum deleniti atque corrupti quos</p></div>
  <div class="step" style="left:880px"><div class="step-icon" role="img" aria-label="Gear with tick icon"></div><h3>Finibus Bonorum</h3><p>At vero eos et accusaus et iusto odio dis ducimus qui blangditiis praentium voluptatum deleniti atque corrupti quos</p></div>

  <svg class="step-arrow" style="left:244px" width="76" height="16" viewBox="0 0 76 16"><path d="M2 10 Q38 2 70 8" fill="none" stroke="#f8ad36" stroke-width="1.5" stroke-dasharray="3 3"/><path d="M66 4 L72 8 L65 11" fill="none" stroke="#f8ad36" stroke-width="1.5"/></svg>
  <svg class="step-arrow" style="left:505px" width="76" height="16" viewBox="0 0 76 16"><path d="M2 10 Q38 2 70 8" fill="none" stroke="#f8ad36" stroke-width="1.5" stroke-dasharray="3 3"/><path d="M66 4 L72 8 L65 11" fill="none" stroke="#f8ad36" stroke-width="1.5"/></svg>
  <svg class="step-arrow" style="left:766px" width="76" height="16" viewBox="0 0 76 16"><path d="M2 10 Q38 2 70 8" fill="none" stroke="#f8ad36" stroke-width="1.5" stroke-dasharray="3 3"/><path d="M66 4 L72 8 L65 11" fill="none" stroke="#f8ad36" stroke-width="1.5"/></svg>
</section>

<section class="about">
  <div class="abs about-photo" role="img" aria-label="Businesswoman looking up while holding a phone in a city at night"></div>
  <h2>About Us</h2>
  <p>At vero eos et accusamus et iusto odio dignmos ducimus qui blanditiis praesem volupum deleniti ate corrupti quos dolores et quas molestias excepturi sinecati cupiditate non provident, similique sunt in culpa qui officia desrunt mollitia animi, id est laborum et dolorum fuga. Et haum quidem rerum facilis est et expedita distinctio. Nam libero tempore, cum soluta nobis est eligendi optio cumque nihil impeit quo minus id quod maxime placeat facere possimus</p>
  <a class="btn" style="left:655px;top:399px;width:148px;height:40px;font-size:14px">Get Started</a>
</section>

<section class="boost">
  <h2>Where Do You Need to Boost Signals ?</h2>
  <div class="building" style="left:65px">
    <div class="circle"><svg width="40" height="36" viewBox="0 0 40 36"><path d="M20 2 L38 18 H33 V34 H24 V24 H16 V34 H7 V18 H2 Z" fill="#fff"/></svg></div>
    <h3>SMALL BUILDING</h3><p>upto 300 m2</p>
  </div>
  <div class="building" style="left:318px">
    <div class="circle"><svg width="30" height="40" viewBox="0 0 30 40"><rect x="2" y="2" width="26" height="36" fill="#fff"/><g fill="#e9962a"><rect x="7" y="7" width="5" height="5"/><rect x="18" y="7" width="5" height="5"/><rect x="7" y="16" width="5" height="5"/><rect x="18" y="16" width="5" height="5"/><rect x="12" y="28" width="6" height="10"/></g></svg></div>
    <h3>MEDIUM BUILDING</h3><p>upto 300 m2</p>
  </div>
  <div class="building" style="left:568px">
    <div class="circle"><svg width="40" height="40" viewBox="0 0 40 40"><rect x="4" y="14" width="14" height="24" fill="#fff"/><rect x="20" y="4" width="16" height="34" fill="#fff"/><g fill="#e9962a"><rect x="8" y="19" width="6" height="4"/><rect x="8" y="27" width="6" height="4"/><rect x="24" y="10" width="8" height="4"/><rect x="24" y="18" width="8" height="4"/><rect x="24" y="26" width="8" height="4"/></g></svg></div>
    <h3>LARGE BUILDING</h3><p>upto 1000 m2</p>
  </div>
  <div class="building" style="left:841px">
    <div class="circle"><svg width="44" height="40" viewBox="0 0 44 40"><rect x="2" y="16" width="12" height="22" fill="#fff"/><rect x="15" y="4" width="14" height="34" fill="#fff"/><rect x="30" y="16" width="12" height="22" fill="#fff"/><g fill="#e9962a"><rect x="19" y="9" width="6" height="4"/><rect x="19" y="17" width="6" height="4"/><rect x="19" y="25" width="6" height="4"/><rect x="5" y="21" width="6" height="3"/><rect x="33" y="21" width="6" height="3"/><rect x="5" y="28" width="6" height="3"/><rect x="33" y="28" width="6" height="3"/></g></svg></div>
    <h3>VERY LARGE BUILDING</h3><p>upto 2000 m2</p>
  </div>
</section>

<section class="help">
  <div class="abs help-photo" role="img" aria-label="Smiling man in a white t-shirt looking at his phone, with yellow and black signal bars behind him"></div>
  <h2>Help Customers discover what’s nearby and decide where to stay</h2>
  <p>Lorem ipsum dolor sit amet, consectetur adipiscing elit, sed do eiusmod tempor incidnt ut labore et dolore magna aliqua. Quis ipsum suspendisse ultricesda.</p>
  <a class="btn" style="left:678px;top:325px;width:147px;height:41px;font-size:14px">Contact Us</a>
</section>

<section class="cases">
  <h2 class="section-title" style="top:72px">Case Studies</h2>
  <p class="section-sub" style="top:118px">Lorem ipsum dolor sit amet, consectetur adipiscing elit, sed do eius</p>

  <div class="case" style="left:99px;top:171px;width:601px;height:223px">
    <div class="case-text" style="left:0;top:32px;width:337px"><h3>The standard Lorem Ipsum pas sage, used since</h3><p>Lorem ipsum dolor sit amet, sectetur adipisg elit, sed do eiusmod tempor incidint ut labore et dolore magna aliqua. Lorem ipsum dolor sit amet, sectetur</p></div>
    <div class="case-img" style="left:337px;top:0;width:264px;height:223px;background:linear-gradient(135deg,#0a2a6b,#2c6fc0 50%,#0b1f4d)" role="img" aria-label="Signal booster device with antennas on a blue tech background"></div>
  </div>

  <div class="case" style="left:99px;top:416px;width:601px;height:220px">
    <div class="case-text" style="left:0;top:32px;width:337px"><h3>The standard Lorem Ipsum pas sage, used since</h3><p>Lorem ipsum dolor sit amet, sectetur adipisg elit, sed do eiusmod tempor incidint ut labore et dolore magna aliqua. Lorem ipsum dolor sit amet, sectetur</p></div>
    <div class="case-img" style="left:337px;top:0;width:264px;height:220px;background:linear-gradient(135deg,#6b3318,#a45a2e 50%,#5a2a12)" role="img" aria-label="Plug-in signal repeater in a wall socket on a wooden wall"></div>
  </div>

  <div class="case" style="left:725px;top:171px;width:376px;height:465px">
    <div class="case-img" style="left:0;top:0;width:376px;height:253px;background:linear-gradient(135deg,#8a8a8a,#4a4a4a 50%,#9b9b9b)" role="img" aria-label="Hands over a laptop keyboard next to a smartphone"></div>
    <div class="case-text" style="left:0;top:276px;width:376px"><h3>The standard Lorem Ipsum pas sage, used since</h3><p>Lorem ipsum dolor sit amet, sectetur adipisg elit, sed do eiusmod tempor incidint ut labore et dolore magna aliqua. Lorem ipsum dolor sit amet, sectetur</p></div>
  </div>
</section>

<section class="contact">
  <h2 class="section-title" style="top:92px">Get In Touch</h2>
  <p class="section-sub" style="top:138px">Lorem ipsum dolor sit amet, consectetur adipiscing elit, sed do eius</p>

  <div class="field" style="left:99px;top:191px;width:295px;height:50px">Name*</div>
  <div class="field" style="left:409px;top:191px;width:293px;height:50px">Company*</div>
  <div class="field" style="left:99px;top:255px;width:295px;height:50px">Email*</div>
  <div class="field" style="left:409px;top:255px;width:293px;height:50px">Contact Number*</div>
  <div class="field" style="left:99px;top:320px;width:603px;height:138px">Your question*</div>
  <a class="btn" style="left:99px;top:475px;width:175px;height:42px;font-size:14px">Send Message</a>

  <div class="info-card">
    <div>Call us on &nbsp;<span class="link">+1 555-014-2290</span></div>
    <div>Email Us &nbsp;&nbsp;&nbsp;<span class="link">info@nestorbolt.com</span></div>
    <div class="link" style="margin-top:10px">Visit us at</div>
    <div>48 Larkmoor Lane Eastfield,<br>US 40218</div>
    <div class="link" style="margin-top:12px;display:flex;align-items:center;gap:10px">
      <svg width="12" height="16" viewBox="0 0 12 16"><path d="M6 0 C2.7 0 0 2.6 0 5.8 C0 10 6 16 6 16 S12 10 12 5.8 C12 2.6 9.3 0 6 0 Z" fill="#3f8fc9"/><circle cx="6" cy="6" r="2.2" fill="#fff"/></svg>
      <span style="border-bottom:1px solid #3f8fc9;line-height:22px">Get directions / view on Wayfold maps</span>
    </div>
  </div>
</section>

<footer class="footer">
  <div class="footer-brand">Nestor Bolt</div>
  <div class="fcol" style="left:414px"><h4>QUICK LINKS</h4><ul><li>Home</li><li>How it works</li><li>Case Studies</li><li>Contact</li></ul></div>
  <div class="fcol" style="left:663px"><h4>CONTACT US</h4><ul>
    <li style="line-height:17px;align-items:flex-start;margin-top:8px"><svg width="9" height="12" viewBox="0 0 12 16" style="margin-top:3px"><path d="M6 0 C2.7 0 0 2.6 0 5.8 C0 10 6 16 6 16 S12 10 12 5.8 C12 2.6 9.3 0 6 0 Z" fill="#fff"/></svg><span>48 Larkmoor Lane<br>Eastfield, US 40218</span></li>
    <li style="margin-top:14px"><svg width="11" height="11" viewBox="0 0 24 24"><path d="M6.6 10.8a15 15 0 0 0 6.6 6.6l2.2-2.2c.3-.3.7-.4 1-.2 1.1.4 2.3.6 3.6.6.6 0 1 .4 1 1V20c0 .6-.4 1-1 1A17 17 0 0 1 3 4c0-.6.4-1 1-1h3.5c.6 0 1 .4 1 1 0 1.3.2 2.5.6 3.6.1.3 0 .7-.2 1z" fill="#fff"/></svg>+1 555-014-2290</li>
    <li style="margin-top:6px"><svg width="12" height="9" viewBox="0 0 12 9"><rect width="12" height="9" fill="#fff"/><path d="M0 0 L6 5 L12 0" fill="none" stroke="#1c1c1c" stroke-width="1.2"/></svg>info@nestorbolt.com</li>
  </ul></div>
  <div class="fcol" style="left:963px"><h4>OTHER LINK</h4><ul><li>Privacy policy</li><li>Terms and condition</li><li>Sitemap</li><li>Help</li></ul></div>
  <div class="footer-rule"></div>
  <div class="copy">©Copyright ©2023 Nestor Bolt. All Rights Reserved.</div>
</footer>

</body>
</html>
```